Business Card

We are looking to re-create our business card. Attached is the company logo. we would like it to be back and front. for example one side with the persons information and the other side with the company logo. Be as creative as you would like but also keep in mind, we are a Health Insurance company and we need to look professional as well.
Business

```html
<!DOCTYPE html>
<html lang="en">
<head>
<meta charset="utf-8">
<title>Meridian Care Group – Business Card</title>
<link href="https://fonts.googleapis.com/css2?family=Source+Sans+3:wght@400;600&display=swap" rel="stylesheet">
<style>
  :root {
    --backdrop: #e6e7e9;
    --paper: #ffffff;
    --slate: #9d9d9f;
    --slate-dark: #8a8a8c;
    --brand-blue: #1a94d6;
    --ink-light: #ffffff;
  }
  * { box-sizing: border-box; margin: 0; padding: 0; }
  html, body { width: 1200px; height: 566px; overflow: hidden; }
  body {
    background: var(--backdrop);
    font-family: "Source Sans 3", "Open Sans", Arial, sans-serif;
    position: relative;
  }
  .card {
    position: absolute;
    top: 134px;
    width: 520px;
    height: 298px;
    background: var(--paper);
    box-shadow: 0 6px 16px rgba(0,0,0,.18);
    overflow: hidden;
  }
  /* Contact side */
  .card--contact { left: 50px; }
  .contact__logo {
    position: absolute; left: 30px; top: 44px;
    display: flex; align-items: center; gap: 8px;
    color: var(--slate); font-weight: 600; font-size: 24px;
  }
  .contact__logo-mark { width: 14px; height: 14px; background: var(--brand-blue); }
  .contact__band {
    position: absolute; left: 0; right: 0; top: 96px; height: 140px;
    background: var(--slate);
    border-top: 4px solid var(--brand-blue);
    border-bottom: 4px solid var(--brand-blue);
  }
  .contact__stripe {
    position: absolute; left: 0; right: 0; bottom: 14px; height: 5px;
    background: var(--brand-blue);
  }
  .contact__person {
    position: absolute; left: 22px; top: 168px;
    display: flex; gap: 12px; align-items: flex-start;
    color: var(--ink-light);
  }
  .contact__avatar {
    width: 24px; height: 24px; background: var(--brand-blue);
    display: flex; align-items: center; justify-content: center;
  }
  .contact__name { font-size: 17px; font-weight: 600; line-height: 1.1; }
  .contact__role { font-size: 15px; padding-left: 6px; }
  .contact__list {
    position: absolute; right: 18px; top: 64px;
    list-style: none; color: var(--ink-light);
  }
  .contact__list li {
    display: flex; align-items: center; justify-content: flex-end; gap: 10px;
    height: 32px; font-size: 11px; text-align: right; line-height: 1.15;
  }
  .contact__list li:first-child { color: var(--slate-dark); }
  .contact__list li:last-child { height: 40px; }
  .icon-box {
    width: 22px; height: 22px; flex: none;
    background: var(--brand-blue);
    display: flex; align-items: center; justify-content: center;
  }
  /* Brand side */
  .card--brand {
    left: 630px;
    background: var(--slate);
    padding: 14px;
  }
  .brand__frame {
    width: 100%; height: 100%;
    border: 4px solid var(--brand-blue);
    background: var(--paper);
    display: flex; align-items: center; justify-content: center;
  }
  .brand__logo {
    display: flex; align-items: center; gap: 14px;
    color: var(--slate); font-weight: 600; font-size: 38px;
  }
  .brand__logo-mark { width: 26px; height: 26px; background: var(--brand-blue); }
</style>
</head>
<body>

<section class="card card--contact" aria-label="Card front with contact details">
  <div class="contact__logo"><span>Meridian Care</span><span class="contact__logo-mark"></span></div>

  <div class="contact__band"></div>
  <div class="contact__stripe"></div>

  <div class="contact__person">
    <span class="contact__avatar">
      <svg width="14" height="14" viewBox="0 0 14 14"><circle cx="7" cy="4.5" r="3" fill="#fff"/><path d="M1 14c0-4 2.7-5.5 6-5.5s6 1.5 6 5.5z" fill="#fff"/></svg>
    </span>
    <div>
      <p class="contact__name">Your Name</p>
      <p class="contact__role">Designation</p>
    </div>
  </div>

  <ul class="contact__list">
    <li><span>555 014 2270</span>
      <span class="icon-box"><svg width="12" height="14" viewBox="0 0 12 14"><rect x="2" y="1" width="8" height="12" rx="1.5" fill="none" stroke="#fff" stroke-width="1.4"/></svg></span></li>
    <li><span>www.meridiancare-example.com</span>
      <span class="icon-box"><svg width="14" height="14" viewBox="0 0 14 14"><circle cx="7" cy="7" r="5.5" fill="none" stroke="#fff" stroke-width="1.4"/><path d="M1.5 7h11M7 1.5c-2.5 3-2.5 8 0 11M7 1.5c2.5 3 2.5 8 0 11" fill="none" stroke="#fff" stroke-width="1"/></svg></span></li>
    <li><span>hello@meridiancare-example.com</span>
      <span class="icon-box"><svg width="14" height="10" viewBox="0 0 14 10"><rect x="0.7" y="0.7" width="12.6" height="8.6" fill="none" stroke="#fff" stroke-width="1.4"/><path d="M1 1l6 5 6-5" fill="none" stroke="#fff" stroke-width="1.2"/></svg></span></li>
    <li><span>48 Linden Avenue,<br>Fairhaven CA 90000</span>
      <span class="icon-box"><svg width="10" height="14" viewBox="0 0 10 14"><path d="M5 13.5S0.8 8 0.8 5a4.2 4.2 0 0 1 8.4 0C9.2 8 5 13.5 5 13.5z" fill="#fff"/><circle cx="5" cy="5" r="1.6" fill="#1a94d6"/></svg></span></li>
  </ul>
</section>

<section class="card card--brand" aria-label="Card back with company name">
  <div class="brand__frame">
    <div class="brand__logo"><span>Meridian Care Group</span><span class="brand__logo-mark"></span></div>
  </div>
</section>

</body>
</html>
```